Lumavane Overview - 2 page brochure

Take our 2-page Word overview and make it pretty! We're trying to install our floating solar system on bodies of water (ponds, reservoirs, etc.) owned by public water agencies. Benefits we want to highlight for the water agencies include: we pay 100% of all costs and sell them the electricity generated at a substantial discount below what they're paying for power today, reduces evaporation, reduces algae growth (this is a big hot button for water agencies since algae clogs up their pumps & filters), reduces CO2 and they earn a lease payment for leasing the water surface to us. We have gone through wind tunnel testing, have filed numerous provisional patent applications, 3rd party engineering reports, and a 6-month test of our system by the California BLRI (Bureau of Levee and Reservoir Integrity) and the Tamrick Valley Water Agency.

Target Market(s)

Water agencies

Industry/Entity Type

Water Company

Font styles to use
Serif

Colors

Designer to choose colors to be used in the design.

Requirements
Must have
• The images I included in the Word file, and most of the text. It has to be 2 pages max.
Nice to have
• All of the text we wrote (not required though).

```html
<!DOCTYPE html>
<html lang="en">
<head>
<meta charset="utf-8">
<title>Lumavane Overview</title>
<link href="https://fonts.googleapis.com/css2?family=Source+Sans+3:wght@400;600;700&display=swap" rel="stylesheet">
<style>
:root{
  --bg:#eeeae4;
  --paper:#ffffff;
  --ink:#2b2b2b;
  --teal:#1c9aab;
  --teal-dark:#137f8e;
  --accent:#1e8fb6;
  --green:#8cc540;
  --muted:#666;
  --photo-water:#6d8fa6;
  --photo-land:#b79a6a;
}
*{box-sizing:border-box;margin:0;padding:0}
html,body{width:1200px;height:960px;overflow:hidden;background:var(--bg)}
body{font-family:"Source Sans 3",sans-serif;color:var(--ink)}
.sheet{position:absolute;left:229px;top:0;width:836px;height:1082px;background:var(--paper);transform:scale(.8873);transform-origin:0 0;overflow:hidden}
.abs{position:absolute}
p,li{font-size:12px;line-height:16px}
sup{font-size:7px;line-height:0;vertical-align:super}
.budget{left:33px;top:28px;width:600px}
.budget h2{font-size:12.5px;font-weight:700}
.budget p{line-height:16.5px}
.hl{color:var(--accent)}
.photo{background:linear-gradient(180deg,#8fb4c9 0%,var(--photo-water) 55%,#3d5d74 100%)}
.proto{left:640px;top:24px;width:162px;height:118px}
.proto span{position:absolute;left:6px;top:3px;color:#fff;font-size:10px;font-weight:700;line-height:12px}
.options{left:33px;top:144px;width:775px}
.band{left:0;top:190px}
.assemble{left:35px;top:200px;width:214px;height:152px;border:3px solid #fff;background:linear-gradient(180deg,#7ea8cf 0%,#8f9a5e 45%,#e0703a 80%,#c9542a 100%)}
.assemble span{position:absolute;right:8px;top:6px;color:#fff;font-size:11px;font-weight:600}
.thumb{border:3px solid #fff;background:linear-gradient(135deg,var(--photo-land),#5d7a5a 60%,#2f4a5a)}
.map{left:543px;top:203px;width:262px;height:152px;border:3px solid #fff;background:linear-gradient(90deg,#f4f4f4 0 34%,#b79b73 34% 100%)}
.cap{color:#fff;font-size:11.5px;font-weight:600;line-height:13px;white-space:nowrap}
.pill{left:208px;top:392px;width:420px;height:30px;border-radius:15px;background:var(--green);color:#fff;font-size:20px;text-align:center;line-height:30px}
.col{top:430px;list-style:none}
.col li{display:flex;font-size:11.5px;line-height:15.6px}
.col li b{color:var(--accent);font-weight:400;width:22px;flex:none}
.col-left{left:33px;width:382px}
.col-right{left:418px;width:390px}
.section{left:33px;width:775px}
.section h3{color:var(--accent);font-size:12.5px;font-weight:600;line-height:16px}
.section h3 .inline{color:var(--ink);font-weight:400;font-size:12px}
.media{left:70px;top:975px;width:700px}
.media h4{position:absolute;left:0;top:2px;font-size:12.5px;font-weight:600}
.outlets{position:absolute;left:106px;top:0;width:590px;display:flex;flex-wrap:wrap;gap:8px 10px;align-items:center}
.outlet{font-size:10.5px;font-weight:600;color:#4a5a66;display:flex;align-items:center;gap:3px;height:18px}
.outlet i{display:inline-block;width:9px;height:9px;background:#4a5a66}
.badge{width:18px;height:18px;border-radius:50%;background:#c8d3d8}
.footer{left:0;top:1030px;width:836px;height:52px;background:var(--teal);padding:11px 33px}
.footer p{color:#fff;font-size:8px;line-height:11px}
</style>
</head>
<body>
<div class="sheet">
  <div class="abs budget">
    <h2>Budgetary Price Estimates:<sup>4</sup></h2>
    <p>a) <span class="hl">20-25¢</span> per watt DC for Lumavane®</p>
    <p>b) <span class="hl">30¢</span> per watt DC for Lumavane Tracker®</p>
    <p>c) <span class="hl">5¢</span> per watt DC for installation of either Lumavane® or Lumavane Tracker® incl. anchors.</p>
    <p>d) <span class="hl">5¢</span> per watt DC for installation of solar panels, inverters, transformer(s) and switchgear.</p>
    <p>e) <span class="hl">$1.00</span> per watt DC or less for most turnkey systems.</p>
  </div>
  <div class="abs photo proto" role="img" aria-label="Child standing on the third Gamma prototype float on a pond"><span>Child standing on<br>Gamma Γ (3rd) Prototype</span></div>
  <p class="abs options"><b>Options available:</b> auto-wash panel rinsing system, extra walkways, electric cart(s) &amp; stoppers for the metal rails, security lighting, security HD video cameras, turnkey project development services (engineering, permitting, utility interconnection process management, etc.), and turnkey installation.</p>

  <svg class="abs band" width="836" height="204" viewBox="0 0 836 204" aria-hidden="true">
    <path d="M0 40 Q220 0 440 12 L836 6 L836 150 Q800 200 640 202 L0 202 Z" fill="var(--teal)"/>
  </svg>
  <div class="abs assemble" role="img" aria-label="Workers assembling orange floats on a shore"><span>Easy to Assemble</span></div>
  <div class="abs thumb" style="left:265px;top:200px;width:60px;height:65px" role="img" aria-label="Aerial view of 2 MW pond"></div>
  <div class="abs thumb" style="left:333px;top:200px;width:62px;height:65px" role="img" aria-label="Aerial view of 5 MW pond"></div>
  <div class="abs thumb" style="left:403px;top:200px;width:122px;height:55px" role="img" aria-label="Aerial view of 3 MW and 1.5 MW ponds"></div>
  <div class="abs thumb" style="left:265px;top:283px;width:62px;height:62px" role="img" aria-label="Aerial view of 1 MW pond"></div>
  <div class="abs thumb" style="left:335px;top:283px;width:62px;height:62px" role="img" aria-label="Aerial view of 1 MW pond"></div>
  <div class="abs thumb" style="left:411px;top:263px;width:80px;height:68px" role="img" aria-label="Aerial view of 2 MW pond"></div>
  <div class="abs map" role="img" aria-label="Site plan and aerial map of a 9 MW floating array on a reservoir"></div>
  <p class="abs cap" style="left:272px;top:360px">Tamrick Valley wastewater ponds going solar</p>
  <p class="abs cap" style="left:546px;top:360px">9 MW: Harlow Reservoir,<br>Brenmoor County Water Authority</p>

  <div class="abs pill">Lumavane Advantages vs. Competitors:</div>

  <ol class="abs col col-left">
    <li><b>1.</b>Cost-competitive with highest project IRR available</li>
    <li><b>2.</b><span>Up to 10% more kWh than plastic floating solar<sup>5</sup></span></li>
    <li><b>3.</b>Made in USA (manufactured in California)</li>
    <li><b>4.</b>75-year design life, 50-year+ expected life</li>
    <li><b>5.</b>Armature is aluminum, not plastic = structural strength</li>
    <li><b>6.</b><span>Floats are shaded by their solar panels: less sun damage over time; no “leakage” of plastic particles into water</span></li>
    <li><b>7.</b><span>Can accommodate any solar panel size. Want to upgrade your panels someday? No problem.</span></li>
    <li><b>8.</b>Flexible row density (GCR) = ↓ inter-row shading</li>
    <li><b>9.</b>Flexible panel tilt (5°-22°); 22° = 8% ↑ kWh than 5°</li>
    <li><b>10.</b>30-75% fewer anchors (subject to size &amp; Geotech)</li>
    <li><b>11.</b>Plastic is HDPE (High Density Poly-Ethylene)</li>
    <li><b>12.</b><span>Our floats are Roto-Molded for uniform wall thickness, whereas Blow-Molding creates thin spots in wall thickness.</span></li>
    <li><b>13.</b>Wind tunnel tested</li>
    <li><b>14.</b>No floor anchors needed (lined or unlined ponds)</li>
  </ol>
  <ol class="abs col col-right" start="15">
    <li><b>15.</b>100% recyclable (aluminum has high recycle value)</li>
    <li><b>16.</b><span>Metal rails allow for an optional electric cart to quickly zip workers &amp; materials from one end to the other.</span></li>
    <li><b>17.</b>Can upgrade to Lumavane Tracker for ↑ kWh</li>
    <li><b>18.</b>Easy maintainability</li>
    <li><b>19.</b>High durability in extreme conditions</li>
    <li><b>20.</b><span>Floats with internal holes for rail bolts; much stronger than protruding / overhanging ear attachment points.</span></li>
    <li><b>21.</b>Bankable with institutional lenders (3rd party IE)</li>
    <li><b>22.</b>Non-toxic &amp; environmentally friendly for full life</li>
    <li><b>23.</b>Rounded underside: won’t beach (get stuck) in mud or silt</li>
    <li><b>24.</b><span>Custom Lumavane® molded floats based on industry gold-standard, time tested Dredging Floats.</span></li>
    <li><b>25.</b><span>Dredging Float’s cylindrical geometry has a proven track record of plastic cost efficiencies and mechanical strength.</span></li>
    <li><b>26.</b>Float top sheds water. No pooling water = no mosquito habitat.</li>
    <li><b>27.</b>25-year warranty.</li>
  </ol>

  <div class="abs section" style="top:704px">
    <h3>Other Applications:</h3>
    <p><b>A)&nbsp; Mollusk / bivalve habitat</b> – we’re developing a sub-surface system hanging underneath the Lumavane to support bivalve colonies such as clams, oysters, mussels and scallops. For bodies of water that could use filtration and/or cleaning, bivalves are a terrific natural re-mediation solution. Available in both freshwater and saltwater.</p>
    <p><b>B)&nbsp; Tracking</b> – we’re developing the Lumavane Tracker, to track the sun (rather than remain in a fixed position) to increase kWh produced annually by up to 35%. This upgrade to Lumavane is possible due to our aluminum frame.</p>
  </div>
  <div class="abs section" style="top:808px">
    <h3>Traction:</h3>
    <p>1. August 2016: after 3 working prototypes were built &amp; tested, commercial v1.0 was wind tunnel tested.</p>
    <p>2. March 2017: completed 6-month test of a small Lumavane system on the Crestline Reservoir in Alder Grove, CA.</p>
    <p>3. April 2017: presented at energy committee of WWPA North-South conference. 115 water agencies want proposals.</p>
    <p>4. May 2017: submitted 99.9% permit design blueprints for 1.3 MW Lumavane system in Tamrick Valley CA.</p>
  </div>
  <div class="abs section" style="top:895px">
    <h3>Intellectual Property: <span class="inline">multiple provisional patent apps filed Nov. 2016 with U.S. Patent &amp; Trademark Office; more pending.</span></h3>
  </div>
  <div class="abs section" style="top:917px">
    <p><span class="hl" style="font-weight:600">Total Addressable Market:</span> through 2025, the global solar industry is expected to add ~500 GW of new solar. Floating solar expected to grow at 45%-65% CAGR. EPA’s Clean Power Plan requires 283 GW of renewables. To power 25% of the USA, ~1,000 GW of solar is needed. 42 GW installed in the US, 271 GW worldwide. Expected growth curve is enormous.</p>
  </div>

  <div class="abs media">
    <h4>Media Coverage:</h4>
    <div class="outlets">
      <span class="outlet"><i></i>Radio Nine</span>
      <span class="outlet">Bay Ledger</span>
      <span class="outlet">Harbor Tribune</span>
      <span class="outlet">Energy Desk</span>
      <span class="outlet">Valley Courier</span>
      <span class="outlet">Grid Engineering</span>
      <span class="outlet">Coastline</span>
      <span class="outlet">Crestline Clean Power</span>
      <span class="badge"></span>
      <span class="outlet">Channel 7</span>
      <span class="outlet">Daily Grid</span>
      <span class="outlet">Solar Frame</span>
      <span class="outlet">Pond Report</span>
      <span class="outlet"><i></i>Meridian</span>
      <span class="outlet">ClearThink</span>
      <span class="outlet">Current Energy</span>
      <span class="outlet">CoPower</span>
      <span class="outlet">Field News</span>
    </div>
  </div>

  <div class="abs footer">
    <p><sup>4</sup>Excludes taxes, freight, permitting costs. Assumes 2 MW ac size, non-union labor. Volume discounts are available for larger projects and/or multiple sites.</p>
    <p><sup>5</sup>Due to increased panel tilt, increased row spacing, cleaner panels, bifacial panels (for albedo reflection) and accommodation of larger more efficient panels.</p>
  </div>
</div>
</body>
</html>
```